Bridgeway, Lantern, and the Quiet Harbor Loop Research Program Website

Overview: This website will serve a new research program (Bridgeway, Lantern, and the Quiet Harbor Loop) at the Fenmoor University School of Medicine. I want a clean, intuitive design that has a navigation bar, but uses icons/graphic buttons to link to the main pages. In an attached Word document, I have provided a basic information architecture for the site, understanding that this project would just generate graphics and code for the 3 pages. I highlighted the 3 pages I'd like designed.
Target market: People who want to participate in our research, or contribute grant funding to specific projects.
Number of page: The design project focuses on 3 pages, but the site must accommodate 6 pages with top-level links. See attached Word doc.
Logo and website header: Please integrate our logo in the header. I've uploaded it as a png file--both with the name of the website and with just the logo image. I imaging the logo would look great in a banner set against an image of a mountain. The two main design themes I want to see included are nature and healthcare.
Text content: I have not yet provided text. Use some dummy text.
Technical Specifications:
- Build using WordPress. We will host this site ourselves on Brimloft using WordPress.
- The design package must be coded.
- The template must be responsive to different platforms (e.g., computer, mobile phone, iPad).
Thank you! I look forward to seeing your designs.
- Ned

```html
<!DOCTYPE html>
<html lang="en">
<head>
<meta charset="utf-8">
<title>Bridgeway, Lantern, and the Quiet Harbor Loop — Research Program</title>
<link href="https://fonts.googleapis.com/css2?family=Poppins:wght@400;500;600;800&family=Dosis:wght@500;600&display=swap" rel="stylesheet">
<style>
:root{
  --teal:#17a98b;
  --teal-dark:#0e8d73;
  --blue:#1350a8;
  --ink:#222;
  --muted:#666;
  --mist:#e4edf5;
  --card-tint:#eef8f5;
  --footer:#1b1f22;
}
*{box-sizing:border-box;margin:0;padding:0}
html,body{width:1200px;height:4501px;overflow:hidden}
body{position:relative;font-family:"Poppins",sans-serif;color:var(--ink);background:#fff}
.abs{position:absolute}
.center{text-align:center}
.heading{font-family:"Dosis",sans-serif;font-weight:600;color:var(--blue)}
.sub{color:var(--teal);font-size:15px}
.para{color:var(--muted);font-size:11.5px;line-height:20px}
.ph{position:absolute}

/* header + hero */
.hero{position:absolute;left:0;top:0;width:1200px;height:700px;background:linear-gradient(180deg,#4e5a66 0%,#8d8a78 30%,#a7814f 48%,#5d4a2d 70%,#2f2a1d 100%)}
.topbar{position:absolute;top:10px;right:58px;display:flex;gap:26px;color:#fff;font-size:12px;align-items:center}
.topbar span{display:flex;gap:8px;align-items:center}
.brand{position:absolute;left:61px;top:22px;display:flex;align-items:center;gap:10px}
.brand-mark{width:42px;height:42px;border-radius:50%;background:var(--teal)}
.brand-name{color:var(--teal);font-size:10px;font-weight:600;line-height:13px;width:290px}
.nav{position:absolute;top:44px;right:58px;display:flex;gap:28px;align-items:center;font-size:12.5px;color:#fff}
.nav .on{color:#3ee0bf}
.btn{background:var(--teal);color:#fff;border-radius:22px;display:inline-flex;align-items:center;justify-content:center}
.nav .btn{padding:10px 22px;font-size:12px}
.hero-title{position:absolute;width:1200px;top:222px;text-align:center;font-weight:800;font-size:44px;line-height:50px;color:#fff}
.hero-title b{display:block;color:var(--blue);font-weight:800}
.hero-lead{position:absolute;width:1200px;top:333px;text-align:center;color:#fff;font-size:13px}
.arrow{position:absolute;top:322px;width:40px;height:40px;border-radius:50%;border:1.5px solid #fff;display:flex;align-items:center;justify-content:center}
.pillar{position:absolute;width:122px;height:122px;border-radius:50%;color:#fff;font-size:13px;display:flex;flex-direction:column;align-items:center;justify-content:center;gap:8px;border:2px solid rgba(255,255,255,.5)}

/* vision */
.vision-img{position:absolute;width:212px;height:212px;border-radius:50%;border:2px solid var(--teal);padding:6px}
.vision-img .ph{inset:6px;border-radius:50%}
.badge{position:absolute;left:80px;bottom:-14px;width:52px;height:52px;border-radius:50%;background:#fff;display:flex;align-items:center;justify-content:center}
.badge i{width:30px;height:30px;border-radius:50%;background:var(--teal)}
.col{position:absolute;top:1216px;width:250px;text-align:center}
.col-title{color:var(--blue);font-size:17px;font-weight:500}
.col .para{margin-top:8px;font-size:11px}

/* team */
.tab{position:absolute;top:1929px;height:42px;border-radius:22px;border:1.5px solid var(--teal);color:var(--teal);font-size:14px;display:flex;align-items:center;justify-content:center}
.tab.on{background:var(--teal);color:#fff}
.member{position:absolute;top:2091px;width:225px;height:210px;background:var(--card-tint)}
.avatar{position:absolute;left:59px;top:-53px;width:106px;height:106px;border-radius:50%;background:#cfd6dc;border:4px solid #fff}
.avatar.on{border-color:var(--teal)}
.member h4{position:absolute;top:79px;width:100%;text-align:center;color:var(--blue);font-weight:500;font-size:14px}
.member p{position:absolute;top:107px;left:18px;right:18px;text-align:center;font-size:11px;line-height:18px}

/* projects */
.project{position:absolute;top:2502px;width:278px;height:372px;border:1px solid #ddd;background:#fff}
.project .ph{left:0;top:0;width:100%;height:281px}
.project h4{position:absolute;top:309px;left:18px;font-size:15px;font-weight:500}
.project p{position:absolute;top:334px;left:18px;font-size:11.5px;color:var(--muted)}

/* faq */
.faq-q{position:absolute;left:729px;font-size:14.5px;font-weight:500;width:370px;line-height:21px}
.faq-mark{position:absolute;left:690px;color:var(--teal);font-size:22px;line-height:20px}
.rule{position:absolute;left:690px;width:410px;border-top:1px solid #e2e2e2}

/* resources */
.res{position:absolute;top:3600px;width:421px;height:217px;border:1px solid #e2e2e2;background:#fff;overflow:hidden}
.res .ph{left:0;top:0;width:166px;height:217px;border-radius:0 110px 110px 0}
.res h4{position:absolute;left:192px;top:38px;font-size:17px;font-weight:500}
.res p{position:absolute;left:192px;top:68px;width:200px}
.res a{position:absolute;left:192px;top:158px;font-size:12px;color:var(--blue)}

/* footer */
.footer{position:absolute;left:0;top:4210px;width:1200px;height:291px;background:var(--footer);color:#cfd3d6;font-size:12px}
.footer h5{position:absolute;top:26px;color:var(--teal);font-size:15px;font-weight:500}
.social{position:absolute;top:151px;width:34px;height:34px;border-radius:50%;border:1.5px solid var(--teal)}
.sitemap{position:absolute;left:611px;top:60px;list-style:none;line-height:24px;font-size:12px}
.sitemap li::before{content:"";display:inline-block;width:5px;height:5px;border-radius:50%;background:var(--teal);margin-right:14px;vertical-align:middle}
</style>
</head>
<body>

<!-- HERO -->
<section class="hero">
  <div class="ph" style="inset:0;background:linear-gradient(180deg,rgba(40,52,62,.55),rgba(0,0,0,0) 45%,rgba(20,18,10,.35))" role="img" aria-label="Sunset over a mountain canyon with a winding river"></div>
  <div class="topbar">
    <span><svg width="14" height="14" viewBox="0 0 24 24"><path fill="#17a98b" d="M6.6 10.8a15 15 0 006.6 6.6l2.2-2.2a1 1 0 011-.25 11 11 0 003.6.6 1 1 0 011 1V20a1 1 0 01-1 1A17 17 0 013 4a1 1 0 011-1h3.5a1 1 0 011 1c0 1.25.2 2.45.6 3.6a1 1 0 01-.25 1z"/></svg>123 456 7890</span>
    <span><svg width="15" height="12" viewBox="0 0 24 18"><rect width="24" height="18" rx="2" fill="#17a98b"/><path d="M2 3l10 7 10-7" stroke="#fff" stroke-width="2" fill="none"/></svg>info@blqh.org</span>
  </div>
  <div class="brand"><i class="brand-mark"></i><div class="brand-name">Bridgeway, Lantern, and the Quiet Harbor Loop<br>The Research Program</div></div>
  <nav class="nav">
    <span class="on">Home</span><span>People</span><span>Projects</span><span>FAQs</span><span>Resources</span>
    <span class="btn">CONTACT US</span>
  </nav>
  <h1 class="hero-title">RESEARCH PROGRAM<b>FOR THE BRIGHT FUTURE !</b></h1>
  <p class="hero-lead">We serve a new RESEARCH PROGRAM at the Fenmoor University School of Medicine</p>
  <div class="arrow" style="left:59px;background:rgba(0,0,0,.35)"><svg width="12" height="12" viewBox="0 0 12 12"><path d="M8 1L3 6l5 5" stroke="#fff" stroke-width="2" fill="none"/></svg></div>
  <div class="arrow" style="left:1098px"><svg width="12" height="12" viewBox="0 0 12 12"><path d="M4 1l5 5-5 5" stroke="#fff" stroke-width="2" fill="none"/></svg></div>
  <div class="pillar" style="left:542px;top:367px;background:rgba(19,80,168,.85)">
    <svg width="44" height="34" viewBox="0 0 44 34"><path d="M10 2h24l8 10-20 20L2 12z M2 12h40 M16 2l-4 10 10 20 10-20-4-10" stroke="#fff" stroke-width="2" fill="none"/></svg>Values</div>
  <div class="pillar" style="left:481px;top:472px;background:rgba(23,169,139,.85)">
    <svg width="44" height="36" viewBox="0 0 44 36"><path d="M22 32L6 18a9 9 0 0116-10 9 9 0 0116 10z" stroke="#fff" stroke-width="2" fill="none"/></svg>Healthcare</div>
  <div class="pillar" style="left:594px;top:475px;background:rgba(23,169,139,.85)">
    <svg width="36" height="40" viewBox="0 0 36 40"><circle cx="18" cy="10" r="5" stroke="#fff" stroke-width="2" fill="none"/><path d="M8 38l4-18h12l4 18" stroke="#fff" stroke-width="2" fill="none"/></svg>Spiritual Life</div>
  <svg class="abs" style="left:0;bottom:0" width="1200" height="60" viewBox="0 0 1200 60" preserveAspectRatio="none"><path d="M0 45 C60 35 110 42 170 32 S280 40 330 30 420 36 470 26 560 30 610 12 700 28 760 20 860 28 920 18 1020 30 1080 22 1160 34 1200 26 V60 H0Z" fill="#fff"/></svg>
</section>

<!-- VISION -->
<h2 class="heading abs center" style="top:762px;width:1200px;font-size:36px">Our Vision</h2>
<p class="sub abs center" style="top:817px;width:1200px">Bridgeway, Lantern, and the Quiet Harbor Loop</p>
<p class="sub abs center" style="top:838px;width:1200px;font-size:14px">The Research Program</p>
<p class="para abs center" style="top:870px;left:325px;width:550px;font-size:11px">Lorem Ipsum has been the industry's standard dummy text ever since the 1500s, when an unknown printer took a galley of type and scrambled it to make a type specimen book. It has survived not only five centuries.</p>

<div class="vision-img" style="left:194px;top:956px"><div class="ph" style="background:linear-gradient(180deg,#e8a27a,#c9604a 60%,#5a2a28)" role="img" aria-label="Person beneath a tree at sunset"></div><div class="badge"><i></i></div></div>
<div class="vision-img" style="left:494px;top:956px"><div class="ph" style="background:radial-gradient(circle at 55% 60%,#f2b25a,#7a3a16 45%,#1e0e08)" role="img" aria-label="Young monk holding a candle"></div><div class="badge"><i></i></div></div>
<div class="vision-img" style="left:794px;top:956px"><div class="ph" style="background:radial-gradient(circle at 50% 55%,#f0a33c,#4a3a5a 45%,#141826)" role="img" aria-label="Hands around a glowing planet"></div><div class="badge"><i></i></div></div>

<div class="col" style="left:175px"><h3 class="col-title">People</h3><p class="para">Lorem Ipsum has been the industry's standard dummy text ever since the 1500s, when an unknown printer took a galley of type and scrambled.</p></div>
<div class="col" style="left:475px"><h3 class="col-title">Research Projects</h3><p class="para">Lorem Ipsum has been the industry's standard dummy text ever since the 1500s, when an unknown printer took a galley of type and scrambled.</p></div>
<div class="col" style="left:775px"><h3 class="col-title">FAQs</h3><p class="para">Lorem Ipsum has been the industry's standard dummy text ever since the 1500s, when an unknown printer took a galley of type and scrambled.</p></div>

<!-- PEOPLE -->
<div class="ph" style="left:0;top:1400px;width:840px;height:430px;background:linear-gradient(180deg,var(--mist),#f2f6fa);border-radius:0 60px 0 0"></div>
<div class="abs" style="left:161px;top:1462px;width:450px;height:346px;background:var(--teal);color:#fff;padding:76px 50px 0 51px">
  <h2 style="font-family:'Dosis',sans-serif;font-weight:600;font-size:38px;line-height:40px">People</h2>
  <p style="font-size:14px;margin-top:14px">Bridgeway, Lantern, and the Quiet Harbor Loop</p>
  <p style="font-size:11px;line-height:20px;margin-top:16px;width:300px">Lorem Ipsum has been the industry's standard dummy text ever since the 1500s, when an unknown printer took a galley of type and scrambled it to make a type specimen book. It has survived not only five centuries.</p>
</div>
<div class="ph" style="left:611px;top:1574px;width:428px;height:300px;background:linear-gradient(180deg,#6e7f6c,#a5a8a0 40%,#8b9486 60%,#3c4a3a)" role="img" aria-label="Person sitting on a dock by a calm lake"></div>
<div class="ph" style="left:529px;top:1808px;width:82px;height:66px;background:linear-gradient(180deg,#8f948c,#4b5646)" role="img" aria-label="Lake dock continued"></div>

<div class="tab on" style="left:344px;width:180px">Research Team</div>
<div class="tab" style="left:533px;width:194px">Advisory Committee</div>
<div class="tab" style="left:735px;width:119px">Partners</div>

<div class="member" style="left:128px"><div class="avatar" role="img" aria-label="Team member portrait"></div><h4>Client Name</h4><p class="para">Lorem Ipsum has been the industry's standard dummy text ever since the industry</p></div>
<div class="member" style="left:367px"><div class="avatar on" role="img" aria-label="Team member portrait"></div><h4>Client Name</h4><p class="para">Lorem Ipsum has been the industry's standard dummy text ever since the industry</p></div>
<div class="member" style="left:608px"><div class="avatar" role="img" aria-label="Team member portrait"></div><h4>Client Name</h4><p class="para">Lorem Ipsum has been the industry's standard dummy text ever since the industry</p></div>
<div class="member" style="left:847px"><div class="avatar" role="img" aria-label="Team member portrait"></div><h4>Client Name</h4><p class="para">Lorem Ipsum has been the industry's standard dummy text ever since the industry</p></div>

<!-- PROJECTS -->
<h2 class="heading abs center" style="top:2382px;width:1200px;font-size:36px">Projects</h2>
<p class="sub abs center" style="top:2434px;width:1200px">Bridgeway, Lantern, and the Quiet Harbor Loop</p>
<div class="ph" style="left:0;top:2620px;width:150px;height:220px;background:linear-gradient(180deg,#fff,#eef1f3)" role="img" aria-label="Faint pine forest backdrop"></div>
<div class="ph" style="left:1050px;top:2620px;width:150px;height:220px;background:linear-gradient(180deg,#fff,#eef1f3)" role="img" aria-label="Faint pine forest backdrop"></div>
<svg class="abs" style="left:87px;top:2617px" width="53" height="20" viewBox="0 0 53 20"><path d="M52 10H2M10 3L2 10l8 7" stroke="var(--blue)" stroke-width="2" fill="none"/></svg>
<svg class="abs" style="left:1059px;top:2617px" width="53" height="20" viewBox="0 0 53 20"><path d="M1 10h50M43 3l8 7-8 7" stroke="var(--blue)" stroke-width="2" fill="none"/></svg>
<div class="project" style="left:161px"><div class="ph" style="background:linear-gradient(180deg,#c8c6c2,#6a6560 60%,#3e3a36)" role="img" aria-label="Group seated in a circle at a workshop"></div><h4>Your Personal Spiritual Coach</h4><p>Lorem Ipsum has been the.</p></div>
<div class="project" style="left:461px"><div class="ph" style="background:linear-gradient(180deg,#5c7a52,#9ab0a8 45%,#c7cdc2 70%,#4e5c3e)" role="img" aria-label="Person sitting by a misty mountain lake"></div><h4>Beyond Religion</h4><p>Lorem Ipsum has been the.</p></div>
<div class="project" style="left:760px"><div class="ph" style="background:linear-gradient(180deg,#7f93b8,#3c4e7a 50%,#1f2c54)" role="img" aria-label="Audience at a lecture hall presentation"></div><h4>Turn Your Life Up</h4><p>Lorem Ipsum has been the.</p></div>

<!-- FAQ -->
<div class="ph" style="left:0;top:2960px;width:1200px;height:500px;background:linear-gradient(180deg,#fff 0%,#fff 55%,#e6edf2 100%)"></div>
<div class="ph" style="left:0;top:3080px;width:660px;height:380px;background:linear-gradient(180deg,#dfe6ec 0%,#8a969f 50%,#3a444b 100%)" role="img" aria-label="Hiker standing on a rocky mountain ridge"></div>
<h2 class="heading abs" style="left:690px;top:2964px;font-size:38px;line-height:46px;width:400px">Frequently Asked Questions</h2>
<span class="faq-mark" style="top:3087px">+</span>
<p class="faq-q" style="top:3084px">What makes this project unique?</p>
<p class="para abs" style="left:729px;top:3116px;width:330px;font-size:11px">Lorem Ipsum has been the industry's standard dummy text ever since the when an unknown printer took a galley of type and scrambled has been.</p>
<div class="rule" style="top:3198px"></div>
<span class="faq-mark" style="top:3212px">–</span>
<p class="faq-q" style="top:3213px">Does this Project Assume that the Impact of Religion Is Always Positive?</p>
<div class="rule" style="top:3279px"></div>
<span class="faq-mark" style="top:3295px">–</span>
<p class="faq-q" style="top:3296px">How Can I Collaborate?</p>
<div class="rule" style="top:3333px"></div>
<span class="faq-mark" style="top:3347px">–</span>
<p class="faq-q" style="top:3348px">Will Fenmoor Faculty Lead All Projects?</p>

<!-- RESOURCES -->
<h2 class="heading abs center" style="top:3529px;width:1200px;font-size:36px">Resources</h2>
<div class="ph" style="left:0;top:3760px;width:1200px;height:460px;background:linear-gradient(180deg,#fff 0%,#d6d9db 30%,#8c9196 55%,#3a3f43 85%,#23272a 100%)" role="img" aria-label="Misty pine forest"></div>
<div class="res" style="left:147px"><div class="ph" style="background:radial-gradient(circle at 45% 50%,#c59a6a,#7a4a2c 60%,#3a2216)" role="img" aria-label="Many hands holding a wooden cross"></div><h4>Diverse Religious</h4><p class="para" style="font-size:11px">Lorem Ipsum has been the indust standard text ever Lorem Ipsum has been the industry's standard dummy text ever text.</p><a>Read More &nbsp;›</a></div>
<div class="res" style="left:597px"><div class="ph" style="background:radial-gradient(circle at 50% 50%,#b44a3a,#5a4a3e 55%,#2a2622)" role="img" aria-label="Person in traditional ceremonial dress"></div><h4>Diverse Religious</h4><p class="para" style="font-size:11px">Lorem Ipsum has been the indust standard text ever Lorem Ipsum has been the industry's standard dummy text ever text.</p><a>Read More &nbsp;›</a></div>

<h2 class="heading abs center" style="top:3908px;width:1200px;font-size:38px;line-height:42px">Learn More About<br>Spiritual Traditions !</h2>
<span class="btn abs" style="left:510px;top:4016px;width:180px;height:42px;font-size:14px">CONTACT US</span>

<!-- FOOTER -->
<footer class="footer">
  <div class="abs" style="left:126px;top:35px;width:119px;height:96px;display:flex;align-items:center;justify-content:center;gap:8px;flex-direction:column">
    <i style="width:52px;height:52px;border-radius:50%;background:var(--teal)"></i>
    <span style="color:var(--teal);font-size:12px;font-weight:600">BLQ Program</span>
  </div>
  <i class="social" style="left:130px" aria-label="Social channel"></i>
  <i class="social" style="left:172px" aria-label="Social channel"></i>
  <i class="social" style="left:214px" aria-label="Social channel"></i>

  <h5 style="left:337px">Contact Us</h5>
  <svg class="abs" style="left:337px;top:66px" width="16" height="22" viewBox="0 0 16 22"><path d="M8 21s7-8 7-13A7 7 0 001 8c0 5 7 13 7 13z" fill="none" stroke="var(--teal)" stroke-width="2"/><circle cx="8" cy="8" r="2.5" fill="var(--teal)"/></svg>
  <p class="abs" style="left:369px;top:62px;line-height:19px;font-size:11px">BLQ<br>101 - lorem ipsum simple text<br>print type industry text!</p>
  <svg class="abs" style="left:337px;top:133px" width="16" height="16" viewBox="0 0 24 24"><path fill="#17a98b" d="M6.6 10.8a15 15 0 006.6 6.6l2.2-2.2a1 1 0 011-.25 11 11 0 003.6.6 1 1 0 011 1V20a1 1 0 01-1 1A17 17 0 013 4a1 1 0 011-1h3.5a1 1 0 011 1c0 1.25.2 2.45.6 3.6a1 1 0 01-.25 1z"/></svg>
  <p class="abs" style="left:369px;top:132px">123 456 7890</p>
  <svg class="abs" style="left:337px;top:170px" width="17" height="13" viewBox="0 0 24 18"><rect width="24" height="18" rx="2" fill="#17a98b"/><path d="M2 3l10 7 10-7" stroke="#1b1f22" stroke-width="2" fill="none"/></svg>
  <p class="abs" style="left:369px;top:167px">info@blqh.org</p>

  <h5 style="left:611px">Sitemap</h5>
  <ul class="sitemap"><li>Home</li><li>People</li><li>Projects</li><li>Faq's</li><li>Resources</li><li>Contact</li></ul>

  <h5 style="left:888px">Newsletter Signup !</h5>
  <p class="abs" style="left:888px;top:62px;width:240px;line-height:19px;font-size:11px">Would you like to receive our exclusive update for signup Today !</p>
  <div class="abs" style="left:888px;top:105px;width:250px;height:38px;border-radius:20px;background:#fff;color:#888;font-size:11px;padding:11px 16px">Enter Email *</div>
  <div class="abs" style="left:1102px;top:109px;width:30px;height:30px;border-radius:50%;background:var(--teal);display:flex;align-items:center;justify-content:center"><svg width="14" height="14" viewBox="0 0 24 24"><path d="M2 11L22 2l-7 20-4-8z" fill="#fff"/></svg></div>

  <p class="abs center" style="top:262px;width:1200px;font-size:11px">©BLQ Research Program - 2021 All rights reserved</p>
</footer>

</body>
</html>
```